Bramblecrest Roofing Co. business card design

I am a Roofing contractor in Texas. The name of my company is Bramblecrest Roofing Co. I also offer a few other services (Christmas light installation, gutters, fencing, pressure washing). However my main gig is roofing. Storm restoration and knowledge of the insurance claim process is my specialty.

My colors are black, red and white. I’d like something pretty simple and clean. Modern looking but with a splash of this red tartan pattern.

I have another version of my logo being edited at the moment where the little top part of the F in roofing that’s currently tartan will be changed to just solid red to make it more visible. So if that’s something you can change in your mock up great. But I can provide the full version once the contest is complete

Target Market(s)

Homeowners

Industry/Entity Type

Roofing

Contact Information for Business Card

Darren Pike. 682-555-0193. www.bramblecrest roofing.example Darren@bramblecrestroofing.example

Colors
EB3D1F
EC4F4E
F09395
F8D3D4
FCEDEE

Requirements
Nice to have
• Maybe instead of a business address. I could say serving all DFW Texas or something like that. And maybe add a line somewhere saying deductible assistance? Just a thought

```html
<!DOCTYPE html>
<html lang="en">
<head>
<meta charset="utf-8">
<title>Bramblecrest Roofing Co. – Business Card</title>
<link rel="stylesheet" href="https://fonts.googleapis.com/css2?family=Montserrat:wght@600;700&family=Nunito+Sans:wght@400;600&display=swap">
<style>
  :root {
    --red: #c62a24;
    --red-dark: #a81d19;
    --black: #111111;
    --white: #ffffff;
    --paper: #f4f4f4;
    --ink: #333333;
    --grey-light: #6a6a6a;
    --grey-dark: #3b3b3b;
    --stage: #2a2a2a;
  }
  * { box-sizing: border-box; margin: 0; padding: 0; }
  html, body {
    width: 1200px; height: 1200px; overflow: hidden;
    background: var(--stage);
  }
  .stage {
    width: 1200px; height: 1200px;
    display: flex; flex-direction: column; align-items: center; justify-content: center;
    gap: 44px;
  }
  .card {
    position: relative;
    width: 900px; height: 514px;
    overflow: hidden;
    box-shadow: 0 10px 30px rgba(0,0,0,.45);
  }
  .card--back {
    background: radial-gradient(ellipse at 45% 45%, var(--grey-light) 0%, var(--grey-dark) 100%);
  }
  .card--front {
    background: linear-gradient(160deg, var(--paper) 0%, var(--white) 60%, #f2f2f2 100%);
  }

  .brand {
    position: absolute; left: 50%; transform: translateX(-50%);
    display: flex; flex-direction: column; align-items: center;
  }
  .card--back .brand { top: 140px; }
  .card--front .brand { top: 70px; }
  .brand__circle {
    width: 110px; height: 110px; border-radius: 50%;
    background: var(--red);
    margin-bottom: 14px;
  }
  .brand__name {
    font-family: "Montserrat", sans-serif;
    font-weight: 700;
    color: var(--red);
    text-transform: uppercase;
    text-align: center;
    line-height: 1.05;
    font-size: 30px;
    letter-spacing: 1px;
  }
  .brand__name span { display: block; font-size: 22px; letter-spacing: 3px; }

  .contact {
    position: absolute; left: 62px; top: 240px;
    list-style: none;
    font-family: "Nunito Sans", sans-serif;
    font-size: 17px; color: var(--ink);
  }
  .contact li { display: flex; align-items: center; gap: 12px; height: 30px; }
  .contact svg { width: 16px; height: 16px; fill: var(--red); flex: none; }

  .person {
    position: absolute; right: 90px; top: 318px; text-align: right;
  }
  .person__name {
    font-family: "Montserrat", sans-serif; font-weight: 700;
    font-size: 40px; color: var(--red); line-height: 1;
  }
  .person__role {
    font-family: "Nunito Sans", sans-serif; font-size: 21px;
    color: var(--ink); margin-top: 6px;
  }

  .footer-band { position: absolute; left: 0; bottom: 0; width: 900px; height: 120px; }
  .tagline {
    position: absolute; right: 150px; bottom: 34px;
    font-family: "Nunito Sans", sans-serif; font-size: 22px;
    color: var(--white); letter-spacing: .5px;
  }
</style>
</head>
<body>
<main class="stage">

  <section class="card card--back" aria-label="Card back">
    <div class="brand">
      <div class="brand__circle"></div>
      <p class="brand__name">Bramblecrest<span>Roofing Co.</span></p>
    </div>
  </section>

  <section class="card card--front" aria-label="Card front">
    <div class="brand">
      <div class="brand__circle"></div>
      <p class="brand__name">Bramblecrest<span>Roofing Co.</span></p>
    </div>

    <ul class="contact">
      <li><svg viewBox="0 0 24 24"><path d="M6.6 10.8a15 15 0 0 0 6.6 6.6l2.2-2.2a1 1 0 0 1 1-.25 11.4 11.4 0 0 0 3.6.57 1 1 0 0 1 1 1V20a1 1 0 0 1-1 1A17 17 0 0 1 3 4a1 1 0 0 1 1-1h3.5a1 1 0 0 1 1 1c0 1.25.2 2.45.57 3.6a1 1 0 0 1-.25 1z"/></svg>682-555-0193</li>
      <li><svg viewBox="0 0 24 24"><path d="M2 5h20v14H2z M2 5l10 8 10-8" /></svg>Darren@bramblecrestroofing.example</li>
      <li><svg viewBox="0 0 24 24"><path d="M12 2a10 10 0 1 0 0 20 10 10 0 0 0 0-20zm6.9 6h-3a15 15 0 0 0-1.3-3.6A8 8 0 0 1 18.9 8zM12 4c.8 1.2 1.5 2.5 1.9 4h-3.8c.4-1.5 1.1-2.8 1.9-4zM4.3 14a8 8 0 0 1 0-4h3.4a16 16 0 0 0 0 4zm.8 2h3a15 15 0 0 0 1.3 3.6A8 8 0 0 1 5.1 16zm3-8h-3a8 8 0 0 1 4.3-3.6A15 15 0 0 0 8.1 8zM12 20c-.8-1.2-1.5-2.5-1.9-4h3.8c-.4 1.5-1.1 2.8-1.9 4zm2.3-6H9.7a14 14 0 0 1 0-4h4.6a14 14 0 0 1 0 4zm.3 5.6a15 15 0 0 0 1.3-3.6h3a8 8 0 0 1-4.3 3.6zm1.7-5.6a16 16 0 0 0 0-4h3.4a8 8 0 0 1 0 4z"/></svg>www.bramblecrest roofing.example</li>
      <li><svg viewBox="0 0 24 24"><path d="M12 2a7 7 0 0 0-7 7c0 5 7 13 7 13s7-8 7-13a7 7 0 0 0-7-7zm0 9.5A2.5 2.5 0 1 1 12 6.5a2.5 2.5 0 0 1 0 5z"/></svg>DFW Texas</li>
    </ul>

    <div class="person">
      <p class="person__name">Darren Pike</p>
      <p class="person__role">Founder</p>
    </div>

    <svg class="footer-band" viewBox="0 0 900 120" preserveAspectRatio="none" aria-hidden="true">
      <defs>
        <linearGradient id="bandRed" x1="0" y1="0" x2="1" y2="0">
          <stop offset="0" stop-color="var(--red)"/>
          <stop offset="1" stop-color="var(--red-dark)"/>
        </linearGradient>
      </defs>
      <path d="M0 52 H440 C455 52 458 64 470 64 H0 Z" fill="var(--black)"/>
      <path d="M0 64 H440 C462 64 468 30 500 30 H900 V120 H0 Z" fill="url(#bandRed)"/>
    </svg>
    <p class="tagline">deductible assistance</p>
  </section>

</main>
</body>
</html>
```